Tradeshow Display for Geothermal Installation Company
Green, Cost-effective energy
Tradeshow Display for Geothermal Installation Company - Home and Garden
Creative Brief
We are Brightmoor Powerworks, a company that revolutionizes how people think about green energy. Through geothermal technology, we help homeowners use green energy that's right beneath their feet to save thousands of dollars annually. We are going to be taking this tradeshow display to fairs and home and garden shows to market ourselves to potential buyers. Here's the display we're going to buy: http://www.plinvex.com/Tall-Arch-10ft-Pop-Up-Trade-Show-Display-Graphic-p/ta10g.htm Here's our logo: http://www.brightmoorpowerworks.com/wp-content/uploads/2012/02/logoforweb6atsize1.png Our website is not final, so don't use that as a guide. DO however, use the logo as a guide, and include it in the design. Here's some designs people have done with the same sign: http://www.plinvex.com/PhotoGallery.asp?ProductCode=TA10G We like the one with the lightbulb, the one with the rockers, and the "revitalized" water one. We dislike the "KRV Harbor", "Vendal Trust", and "Quorvane". It needs to have a very dignified, yet undeniably cool feel to the whole thing. Perhaps minimalist. We think Tindle products do a good job of exemplifying this. Sometimes simpler is better. We're excited to see what you come up with!
Home and Garden
Homeowners on the upper end of the income spectrum.
Design must include our logo prominently. Final design must be 159.812"W x 88.98"H, at 125 dpi or higher. For more information go to http://www.plinvex.com/Articles.asp?ID=141 We are buying the Tall Arch 10ft Pop up Tradeshow Display. You can find templates and specifications at the website above.

```html
<!DOCTYPE html>
<html lang="en">
<head>
<meta charset="utf-8">
<title>Brightmoor Powerworks – Tradeshow Display</title>
<link href="https://fonts.googleapis.com/css2?family=Open+Sans:wght@600;700&display=swap" rel="stylesheet">
<style>
  :root {
    --paper: #efefef;
    --paper-light: #f7f7f7;
    --sky-blue: #6ab6e2;
    --sky-blue-deep: #4a9fd6;
    --leaf-green: #a4cf48;
    --leaf-green-light: #c6e184;
    --brand-blue: #1f64b0;
    --tagline-grey: #5a5a5a;
  }
  html, body {
    margin: 0;
    padding: 0;
    overflow: hidden;
    background: var(--paper);
  }
  .display {
    position: relative;
    width: 1200px;
    height: 839px;
    overflow: hidden;
    background: radial-gradient(ellipse at 55% 45%, var(--paper-light), var(--paper) 70%);
    font-family: "Open Sans", Arial, sans-serif;
  }
  .wave-art {
    position: absolute;
    inset: 0;
  }
  .brand {
    position: absolute;
    left: 396px;
    top: 350px;
    display: flex;
    align-items: center;
    gap: 18px;
  }
  .brand-mark {
    width: 72px;
    height: 72px;
    border-radius: 50%;
    background: var(--brand-blue);
  }
  .brand-name {
    margin: 0;
    font-size: 36px;
    font-weight: 700;
    line-height: 1;
    color: var(--brand-blue);
  }
  .tagline {
    position: absolute;
    right: 40px;
    top: 680px;
    margin: 0;
    font-size: 30px;
    font-weight: 600;
    line-height: 1.2;
    color: var(--tagline-grey);
  }
</style>
</head>
<body>
<main class="display">
  <svg class="wave-art" width="1200" height="839" viewBox="0 0 1200 839"
       role="img" aria-label="Decorative blue and green wave artwork framing the left side and bottom">
    <defs>
      <linearGradient id="skyFill" x1="0" y1="0" x2="1" y2="1">
        <stop offset="0" stop-color="var(--sky-blue-deep)"/>
        <stop offset="1" stop-color="var(--sky-blue)"/>
      </linearGradient>
      <linearGradient id="leafFill" x1="0" y1="0" x2="1" y2="0">
        <stop offset="0" stop-color="var(--leaf-green)"/>
        <stop offset="1" stop-color="var(--leaf-green-light)"/>
      </linearGradient>
    </defs>
    <path fill="url(#skyFill)"
      d="M0,0 H180 C100,180 90,380 130,470 C220,600 700,640 1200,560 V660 C800,680 400,660 0,640 Z"/>
    <path fill="url(#leafFill)"
      d="M0,590 C400,560 800,690 1200,620 V650 C900,660 700,720 600,839 H0 Z"/>
  </svg>

  <div class="brand">
    <span class="brand-mark"></span>
    <h1 class="brand-name">Brightmoor Powerworks</h1>
  </div>

  <p class="tagline">Green, Cost-effective energy</p>
</main>
</body>
</html>
```